Professional, Scientific Cover Design for Nutritional / Hair Tissue Mineral Analysis (HTMA) Company

Hair tissue mineral analysis is a versatile, science-backed tool that offers a deeper understanding of your body's mineral and heavy metal profile. By evaluating long-term mineral balance and toxic exposures, HTMA provides invaluable insights that can aid in optimizing nutrition, addressing chronic health issues, and creating a personalized wellness strategy.

We have updated our logo and are in need of an updated report cover in which personalized test results are placed. We are looking for a professional and more modern look.

There are 2 small cutouts that will need to remain as shown in the picture in the brief.

Our updated logo along with color palette used will be uploaded in the brief as well as our 2 previous, outdated designs. We no longer want our address on the front cover. We also do not want images with people in them.

Thank you.

Website: www.pevdosk.com

Designs look the same

• Images with people

```html
<!DOCTYPE html>
<html lang="en">
<head>
<meta charset="utf-8">
<title>Hair Tissue Mineral Analysis – Report Cover</title>
<link rel="stylesheet" href="https://fonts.googleapis.com/css2?family=Krona+One&family=Montserrat:wght@500&display=swap">
<style>
  :root {
    --paper-light: #f7fbfd;
    --sky-pale: #d8e8f2;
    --sky-mid: #7fa7c9;
    --ocean: #2c6a9f;
    --ocean-deep: #17467a;
    --navy: #0e2a55;
    --title-blue: #2b4f9e;
    --cutout: #ffffff;
    --cutout-edge: #d5dde4;
    --brand-text: #ffffff;
  }
  * { margin: 0; padding: 0; box-sizing: border-box; }
  html, body { width: 945px; height: 1200px; overflow: hidden; background: var(--paper-light); }
  .cover {
    position: relative;
    width: 945px;
    height: 1200px;
    overflow: hidden;
    background:
      radial-gradient(ellipse 70% 40% at 38% 6%, #ffffff 0%, rgba(255,255,255,0) 70%),
      linear-gradient(160deg, var(--paper-light) 0%, var(--sky-pale) 30%, var(--sky-mid) 55%, var(--ocean) 75%, var(--ocean-deep) 90%, var(--navy) 100%);
  }
  .cover__waves { position: absolute; inset: 0; width: 945px; height: 1200px; }
  .cover__base {
    position: absolute;
    left: 0; bottom: 0;
    width: 945px; height: 190px;
    background: linear-gradient(180deg, rgba(14,42,85,0) 0%, rgba(14,42,85,0.85) 40%, var(--navy) 100%);
  }
  .cutout {
    position: absolute;
    top: 156px;
    width: 376px;
    height: 38px;
    background: var(--cutout);
    border: 1px solid var(--cutout-edge);
  }
  .cutout--left { left: 95px; }
  .cutout--right { left: 513px; }
  .cover__title {
    position: absolute;
    top: 226px;
    left: 0; right: 0;
    text-align: center;
    font-family: "Krona One", sans-serif;
    font-weight: 400;
    font-size: 50px;
    line-height: 64px;
    color: var(--title-blue);
    letter-spacing: 0.5px;
    padding-left: 36px;
  }
  .cover__art {
    position: absolute;
    left: 0; top: 380px;
    width: 420px; height: 640px;
    background:
      radial-gradient(ellipse 55% 45% at 35% 55%, rgba(40,78,128,0.55) 0%, rgba(40,78,128,0.2) 55%, rgba(40,78,128,0) 80%),
      radial-gradient(circle at 55% 40%, rgba(214,120,70,0.25) 0%, rgba(214,120,70,0) 35%);
    border-radius: 0 50% 50% 0;
  }
  .brand {
    position: absolute;
    left: 0; right: 0;
    top: 1072px;
    display: flex;
    justify-content: center;
    align-items: center;
    gap: 14px;
  }
  .brand__dot {
    width: 18px; height: 18px;
    border-radius: 50%;
    background: var(--brand-text);
  }
  .brand__name {
    font-family: "Montserrat", sans-serif;
    font-weight: 500;
    font-size: 30px;
    letter-spacing: 3px;
    color: var(--brand-text);
    text-transform: uppercase;
  }
</style>
</head>
<body>
  <main class="cover">
    <svg class="cover__waves" viewBox="0 0 945 1200" aria-hidden="true">
      <path d="M0 760 C 260 640, 520 560, 945 300" fill="none" stroke="rgba(255,255,255,0.35)" stroke-width="3"/>
      <path d="M0 820 C 300 700, 560 620, 945 380" fill="none" stroke="rgba(255,255,255,0.22)" stroke-width="2"/>
      <path d="M0 900 C 280 820, 600 760, 945 560 L945 1200 L0 1200 Z" fill="rgba(20,70,125,0.25)"/>
      <path d="M560 1200 C 700 980, 820 760, 945 620" fill="none" stroke="rgba(255,255,255,0.18)" stroke-width="2"/>
    </svg>

    <div class="cover__art" role="img" aria-label="Illustration of a glossy blue and copper molecular structure"></div>

    <div class="cover__base"></div>

    <div class="cutout cutout--left"></div>
    <div class="cutout cutout--right"></div>

    <h1 class="cover__title">Hair Tissue<br>Mineral Analysis</h1>

    <div class="brand">
      <span class="brand__dot"></span>
      <span class="brand__name">Pevdosk Laboratories</span>
    </div>
  </main>
</body>
</html>
```